Bref créative
logo for mining tool supplier
Durable Quarry Fittings
Professional
Luka Vranek
Manager
42 Tindale ave
Wirrabong NSW 2581
sales@quarry-fittings.com.au
quarry-fittings.com.au

```html
<!DOCTYPE html>
<html lang="en">
<head>
<meta charset="utf-8">
<title>Durable Quarry Fittings – Business Card</title>
<link rel="stylesheet" href="https://fonts.googleapis.com/css2?family=Montserrat:wght@400;600&display=swap">
<style>
  :root {
    --bg: #e9ecef;
    --card: #ffffff;
    --orange: #f26a1b;
    --blue: #2ea3e6;
    --ink: #3a3a3a;
    --white: #ffffff;
  }
  * { box-sizing: border-box; margin: 0; padding: 0; }
  html, body { width: 1200px; height: 629px; overflow: hidden; }
  body {
    background: var(--bg);
    font-family: "Montserrat", sans-serif;
    display: flex;
    align-items: center;
    justify-content: center;
    gap: 60px;
  }
  .card {
    position: relative;
    width: 500px;
    height: 286px;
    background: var(--card);
    box-shadow: 0 6px 18px rgba(0,0,0,.15);
    overflow: hidden;
  }
  .brand { display: flex; align-items: center; gap: 10px; }
  .brand-square {
    width: 18px; height: 18px;
    background: var(--blue);
    flex: none;
  }
  .brand-name {
    font-weight: 600;
    color: var(--ink);
    font-size: 24px;
    line-height: 1;
  }
  .card-front { display: flex; align-items: center; justify-content: center; }

  .card-back .brand { position: absolute; left: 34px; top: 52px; }
  .card-back .brand-name { font-size: 20px; }
  .card-back .brand-square { width: 15px; height: 15px; }

  .wave { position: absolute; left: 0; bottom: 0; width: 500px; height: 190px; }
  .person {
    position: absolute; left: 300px; top: 124px; color: var(--white);
  }
  .person-name { font-weight: 600; font-size: 13px; }
  .person-role { font-size: 9px; margin-bottom: 10px; }
  .contacts { list-style: none; display: flex; flex-direction: column; gap: 6px; }
  .contacts li { display: flex; align-items: center; gap: 7px; font-size: 9.5px; }
  .contacts svg { width: 13px; height: 13px; flex: none; }
  .address {
    position: absolute; left: 34px; bottom: 22px;
    color: var(--white); font-size: 10px; line-height: 1.4;
  }
</style>
</head>
<body>
  <section class="card card-front">
    <div class="brand">
      <span class="brand-square"></span>
      <span class="brand-name">Durable Quarry Fittings</span>
    </div>
  </section>

  <section class="card card-back">
    <div class="brand">
      <span class="brand-square"></span>
      <span class="brand-name">Durable Quarry Fittings</span>
    </div>

    <svg class="wave" viewBox="0 0 500 190" preserveAspectRatio="none" aria-hidden="true">
      <path d="M0 80 C140 40 300 20 500 0 L500 190 L0 190 Z" fill="var(--blue)"/>
      <path d="M0 62 C150 28 310 12 500 -6 L500 2 C300 24 140 44 0 76 Z" fill="var(--orange)"/>
    </svg>

    <div class="person">
      <p class="person-name">Luka Vranek</p>
      <p class="person-role">Manager</p>
      <ul class="contacts">
        <li>
          <svg viewBox="0 0 16 16"><circle cx="8" cy="8" r="8" fill="#fff"/><path d="M5.2 4.2l1.5 1.6-.8 1a5 5 0 0 0 2.3 2.3l1-.8 1.6 1.5-.8 1.2c-2.6-.2-5.2-2.8-5.4-5.4z" fill="var(--blue)"/></svg>
          0412 608 317
        </li>
        <li>
          <svg viewBox="0 0 16 16"><circle cx="8" cy="8" r="8" fill="#fff"/><rect x="4" y="5" width="8" height="6" fill="none" stroke="var(--blue)" stroke-width="1.2"/><path d="M4 5l4 3.5L12 5" fill="none" stroke="var(--blue)" stroke-width="1.2"/></svg>
          sales@quarry-fittings.com.au
        </li>
        <li>
          <svg viewBox="0 0 16 16"><circle cx="8" cy="8" r="8" fill="#fff"/><circle cx="8" cy="8" r="4" fill="none" stroke="var(--blue)" stroke-width="1.2"/><path d="M4 8h8M8 4v8" stroke="var(--blue)" stroke-width="1"/></svg>
          quarry-fittings.com.au
        </li>
      </ul>
    </div>

    <p class="address">42 Tindale ave<br>Wirrabong NSW 2581</p>
  </section>
</body>
</html>
```